Wordpress Template for Food Retail Shop

We need a wordpress template that fits our new wp installation with about 6-7 sites. frontpage, news, team, products, contact. we provide food from local suppliers, * green * products. we provide a local bakery

```html
<!DOCTYPE html>
<html lang="en">
<head>
<meta charset="utf-8">
<title>Verdan Bakery</title>
<link href="https://fonts.googleapis.com/css2?family=Playfair+Display:wght@400;700&family=Open+Sans:wght@400;600;700&display=swap" rel="stylesheet">
<style>
:root{
  --green:#7cc21f;
  --brown-dark:#3b1f0e;
  --brown:#5a2e14;
  --orange:#d97b25;
  --cream:#f3f1ee;
  --ink:#2b2420;
  --muted:#8a817a;
  --white:#ffffff;
  --chalk:#1f2326;
}
*{box-sizing:border-box;margin:0;padding:0}
html,body{width:1200px;height:3188px;overflow:hidden}
body{position:relative;font-family:"Open Sans",Arial,sans-serif;color:var(--ink);background:var(--white)}
.abs{position:absolute}
.serif{font-family:"Playfair Display",Georgia,serif}

/* header */
.top-stripe{left:0;top:0;width:1200px;height:8px;background:var(--green)}
.site-header{left:0;top:8px;width:1200px;height:112px;background:linear-gradient(var(--brown-dark),var(--brown))}
.brand{left:118px;top:40px;display:flex;align-items:center;gap:10px}
.brand-dot{width:34px;height:34px;border-radius:50%;background:var(--green)}
.brand-name{font-family:"Playfair Display",Georgia,serif;font-weight:700;font-size:30px;color:var(--green);letter-spacing:1px}
.main-nav{left:560px;top:58px;display:flex;gap:40px}
.main-nav a{color:var(--white);font-size:14px;font-weight:600;text-decoration:none}

/* hero */
.hero{left:0;top:120px;width:1200px;height:520px;background:linear-gradient(120deg,#4a2f1e 0%,#8a6244 35%,#c9a987 60%,#6d4a30 100%)}
.hero-title{left:0;top:248px;width:1200px;text-align:center;color:var(--white);font-size:66px;font-weight:700}
.hero-text{left:380px;top:352px;width:440px;text-align:center;color:#f4ece4;font-size:14px;line-height:22px}
.btn{display:inline-block;background:var(--orange);color:var(--white);font-size:12px;font-weight:700;letter-spacing:1px;padding:14px 26px;text-decoration:none}
.hero-btn{left:528px;top:470px}

/* art of bakery */
.art-title{left:200px;top:740px;width:330px;text-align:center;font-size:36px}
.kicker{color:var(--orange);font-size:11px;font-weight:700;letter-spacing:1.5px}
.art-kicker{left:200px;top:794px;width:330px;text-align:center}
.art-text{left:210px;top:830px;width:310px;text-align:center;font-size:13px;line-height:21px;color:var(--muted)}
.avatar{left:330px;top:930px;width:70px;height:70px;border-radius:50%;background:linear-gradient(#6b4a3a,#caa58a)}
.chef-name{left:200px;top:1012px;width:330px;text-align:center;font-size:17px}
.chef-role{left:200px;top:1042px;width:330px;text-align:center;font-size:11px;color:var(--orange)}
.art-card{left:610px;top:735px;width:250px;height:345px;background:var(--white);box-shadow:0 8px 26px rgba(0,0,0,.18);padding:10px}
.art-photo{width:230px;height:325px;background:linear-gradient(160deg,#e9e1d3,#b58a5c 55%,#7a4e2c)}
.art-badge{left:680px;top:860px;width:112px;padding:12px 0;text-align:center;background:rgba(120,70,30,.85);color:#f6e5c9;font-family:"Playfair Display",Georgia,serif;font-size:20px;line-height:24px;letter-spacing:1px}

/* pancakes */
.wood-band{left:0;top:1180px;width:1200px;height:520px;background:linear-gradient(90deg,#5a3a22,#8b5d3b 40%,#b08054 70%,#d9b98a)}
.pancake-card{left:180px;top:1260px;width:590px;height:360px;background:var(--white);box-shadow:0 10px 30px rgba(0,0,0,.3)}
.pancake-photo{left:180px;top:1260px;width:310px;height:360px;background:linear-gradient(150deg,#c03a3f,#e8b070 45%,#7d4a25)}
.pancake-title{left:492px;top:1282px;font-size:30px}
.pancake-kicker{left:492px;top:1328px}
.pancake-text{left:492px;top:1360px;width:250px;font-size:12px;line-height:20px;color:var(--muted)}
.stars{left:492px;top:1450px;color:var(--orange);font-size:16px;letter-spacing:3px}
.thumbs{left:500px;top:1540px;display:flex;gap:24px}
.thumb{width:40px;height:40px;border-radius:50%;background:linear-gradient(#9a3d2a,#e0b27c)}

/* reuben */
.reuben-bg{left:0;top:1700px;width:1200px;height:740px;background:var(--cream)}
.mark{left:560px;top:1760px;width:80px;height:50px;background:#cfc6bc;border-radius:40px 40px 0 0}
.divider{left:808px;top:1736px;width:2px;height:90px;background:var(--ink)}
.reuben-title{left:0;top:1836px;width:1200px;text-align:center;font-size:48px}
.reuben-kicker{left:0;top:1904px;width:1200px;text-align:center}
.menu-list{left:190px;top:2010px;width:260px}
.menu-item{display:flex;gap:16px;margin-bottom:44px}
.menu-thumb{flex:0 0 54px;height:54px;border-radius:50%;background:linear-gradient(#7a4a25,#d7a46a)}
.menu-item h3{font-family:"Playfair Display",Georgia,serif;font-size:16px;margin-bottom:6px}
.menu-item p{font-size:11px;line-height:17px;color:var(--muted)}
.reuben-card{left:480px;top:1990px;width:270px;height:380px;background:var(--white);padding:10px;box-shadow:0 8px 24px rgba(0,0,0,.15)}
.reuben-photo{width:250px;height:360px;background:linear-gradient(160deg,#3a2a20,#a6562e 45%,#e2b57a 70%,#4a3020)}
.stats{left:800px;top:1990px;width:140px;height:380px;background:var(--white);box-shadow:0 8px 24px rgba(0,0,0,.12);display:flex;flex-direction:column;justify-content:space-around;align-items:center;padding:14px 0}
.stat{width:104px;text-align:center;border:1px solid #e3ddd6;padding:10px 0}
.stat b{display:block;font-family:"Playfair Display",Georgia,serif;font-size:40px;font-weight:400;line-height:44px}
.stat span{font-size:10px;letter-spacing:1.5px;color:var(--muted)}

/* breakfast */
.chalk{left:0;top:2440px;width:1200px;height:680px;background:radial-gradient(ellipse at 40% 40%,#3a3f42,var(--chalk) 70%)}
.bread-strip{left:0;top:2900px;width:1200px;height:220px;background:linear-gradient(180deg,rgba(0,0,0,0),#7a5030 40%,#c08a55)}
.baguettes{left:880px;top:2440px;width:320px;height:680px;background:linear-gradient(100deg,rgba(0,0,0,0),#b98350 40%,#e4c08f)}
.bf-title{left:300px;top:2520px;width:300px;text-align:center;color:var(--white);font-size:44px;font-weight:700}
.bf-kicker{left:300px;top:2578px;width:300px;text-align:center}
.bf-list{left:330px;top:2620px;width:240px;text-align:center;color:var(--white)}
.bf-item{margin-bottom:26px}
.bf-item h4{font-family:"Playfair Display",Georgia,serif;font-size:15px;margin-bottom:4px}
.bf-item p{font-size:11px;color:#c9c4bf}
.bf-item .price{color:var(--orange);font-weight:700;font-size:16px;margin-top:6px}
.escape-card{left:600px;top:2500px;width:280px;height:460px;background:var(--white);box-shadow:0 10px 30px rgba(0,0,0,.35);text-align:center}
.escape-icon{position:absolute;left:120px;top:110px;width:40px;height:40px;border-radius:50%;border:2px solid var(--orange)}
.escape-card h3{position:absolute;left:30px;top:180px;width:220px;font-family:"Playfair Display",Georgia,serif;font-size:20px;line-height:28px}
.escape-card p{position:absolute;left:40px;top:252px;width:200px;font-size:11px;line-height:18px;color:var(--muted)}
.escape-card .btn{position:absolute;left:86px;top:350px;background:var(--ink);font-size:10px;padding:10px 22px}

/* footer */
.site-footer{left:0;top:3120px;width:1200px;height:68px;background:linear-gradient(var(--brown),var(--brown-dark))}
.foot-nav{left:0;top:3144px;width:1200px;display:flex;justify-content:center;gap:44px}
.foot-nav a{color:var(--white);font-size:13px;font-weight:600;text-decoration:none}
</style>
</head>
<body>

<div class="abs top-stripe"></div>
<header class="abs site-header"></header>
<div class="abs brand"><span class="brand-dot"></span><span class="brand-name">VERDAN</span></div>
<nav class="abs main-nav"><a href="#">Home</a><a href="#">About</a><a href="#">Recipes</a><a href="#">About</a><a href="#">Blog</a><a href="#">Contact</a></nav>

<section class="abs hero" role="img" aria-label="Rustic wooden table with bread loaves, coffee cup, wheat and scattered grains"></section>
<h1 class="abs hero-title serif">Baked with love</h1>
<p class="abs hero-text">Fresh bread and pastries from local farms, baked every morning with green grain and a lot of care.</p>
<a class="abs btn hero-btn" href="#">OUR MENU</a>

<h2 class="abs art-title serif">Art of Bakery</h2>
<p class="abs kicker art-kicker">WE CREATE DELICIOUS MOMENTS</p>
<p class="abs art-text">Our bakers start before sunrise, shaping dough from local mills and slow rising it for deep flavour. Every loaf, bun and tart leaves our oven warm and honest.</p>
<div class="abs avatar" role="img" aria-label="Portrait of the head baker"></div>
<p class="abs chef-name serif">chef Nora Bell</p>
<p class="abs chef-role">Head baker since the very first day</p>
<div class="abs art-card"><div class="art-photo" role="img" aria-label="Collage of cakes, pastries and baking ingredients"></div></div>
<div class="abs art-badge">TASTES<br>SO GOOD</div>

<section class="abs wood-band" role="img" aria-label="Wooden board with baguettes, croissants and bread baskets"></section>
<div class="abs pancake-card"></div>
<div class="abs pancake-photo" role="img" aria-label="Stack of pancakes topped with raspberries and blueberries"></div>
<h2 class="abs pancake-title serif">Perfect Pancakes</h2>
<p class="abs kicker pancake-kicker">SOFT AND GOLDEN</p>
<p class="abs pancake-text">Fluffy stacks made with farm eggs, fresh milk and seasonal berries, served warm with honey from nearby hives.</p>
<div class="abs stars">★★★★★</div>
<div class="abs thumbs">
  <span class="thumb" role="img" aria-label="Berry dish"></span>
  <span class="thumb" role="img" aria-label="Pastry dish"></span>
  <span class="thumb" role="img" aria-label="Fruit dish"></span>
</div>

<section class="abs reuben-bg"></section>
<div class="abs mark" role="img" aria-label="Small windmill emblem"></div>
<div class="abs divider"></div>
<h2 class="abs reuben-title serif">Reuben Sandwich</h2>
<p class="abs kicker reuben-kicker">TOASTED RYE WITH LOCAL CORNED BEEF</p>
<div class="abs menu-list">
  <div class="menu-item"><span class="menu-thumb" role="img" aria-label="Rye bread"></span><div><h3>Rye spread</h3><p>Whole grain rye from the valley mill.</p></div></div>
  <div class="menu-item"><span class="menu-thumb" role="img" aria-label="Sliced beef"></span><div><h3>Fresh cut</h3><p>Whole grain rye from the valley mill.</p></div></div>
  <div class="menu-item"><span class="menu-thumb" role="img" aria-label="Melted cheese"></span><div><h3>Seal with cheese</h3><p>Whole grain rye from the valley mill.</p></div></div>
</div>
<div class="abs reuben-card"><div class="reuben-photo" role="img" aria-label="Toasted sandwiches with tomatoes on a board"></div></div>
<div class="abs stats">
  <div class="stat"><b>15</b><span>MINS</span></div>
  <div class="stat"><b>35</b><span>MINS</span></div>
  <div class="stat"><b>50</b><span>SERVES</span></div>
</div>

<section class="abs chalk" role="img" aria-label="Dark chalkboard surface"></section>
<div class="abs bread-strip" role="img" aria-label="Row of bread rolls and loaves"></div>
<div class="abs baguettes" role="img" aria-label="Baguettes on a checkered cloth"></div>
<h2 class="abs bf-title serif">Breakfast</h2>
<p class="abs kicker bf-kicker">THE BREAKFAST MENU</p>
<div class="abs bf-list">
  <div class="bf-item"><h4>Full Breakfast</h4><p>Eggs, bacon, beans and toast</p><p class="price">$65.28</p></div>
  <div class="bf-item"><h4>Toast &amp; Jam</h4><p>Sourdough with berry jam</p><p class="price">$4.90</p></div>
  <div class="bf-item"><h4>Pancakes</h4><p>With maple and butter</p></div>
</div>
<div class="abs escape-card">
  <span class="escape-icon"></span>
  <h3>Your Morning Escape With Flair</h3>
  <p>Start the day slow with coffee, warm rolls and fresh fruit from our garden.</p>
  <a class="btn" href="#">READ MORE</a>
</div>

<footer class="abs site-footer"></footer>
<nav class="abs foot-nav"><a href="#">Home</a><a href="#">Menu</a><a href="#">Recipes</a><a href="#">About</a><a href="#">Blog</a><a href="#">Contact</a></nav>

</body>
</html>
```